Advert for Services that we offer

Bolt Remova Ltd need an design to represent what we do in a modern way by showing an image with a brief description and the use of corporate logo the information we will proved vie a doc file and this is to be presented in a modern way. This design will be for print & web. we have done our own design and its not great i have put this in the file repository

Target Market(s)

Motor trade

Font styles to use
Sans Serif

Colors

Designer to choose colors to be used in the design.

Requirements
Must have
• Company colour scheme as per logo within the files uploaded.
• and a small boarder to isolate it from the rest of the articles.
Nice to have
• Modern font
Should not have
• Old style font

```html
<!DOCTYPE html>
<html lang="en">
<head>
<meta charset="utf-8">
<title>Bolt Remova Ltd – Product Testing &amp; Analysis</title>
<link rel="stylesheet" href="https://fonts.googleapis.com/css2?family=Roboto+Condensed:wght@500&family=Roboto:wght@700&family=Open+Sans:wght@500&family=Montserrat:wght@600;800&display=swap">
<style>
  :root {
    --brand-blue: #2373bb;
    --brand-grey: #8e9093;
    --band-grey: #b8b9bc;
    --paper: #ffffff;
    --backdrop: #b0b0b0;
    --photo-light: #c9c9c7;
    --photo-mid: #8d8c8a;
    --photo-warm: #c8482a;
  }
  * { margin: 0; padding: 0; box-sizing: border-box; }
  html, body { width: 1200px; height: 1200px; overflow: hidden; background: var(--backdrop); }
  .advert {
    position: absolute;
    left: 0; top: 212px;
    width: 1084px; height: 700px;
    transform: scale(1.107);
    transform-origin: 0 0;
    background: var(--paper);
    overflow: hidden;
  }
  .advert__shapes { position: absolute; inset: 0; }
  .brand {
    position: absolute; left: 30px; top: 100px; width: 350px;
    display: flex; align-items: center; justify-content: center; gap: 12px;
    white-space: nowrap;
    font-family: "Montserrat", sans-serif; font-weight: 600;
    font-size: 28px; color: var(--brand-blue); letter-spacing: 0.5px;
  }
  .brand__mark { width: 30px; height: 30px; background: var(--brand-blue); flex: none; }
  .headline { position: absolute; left: 27px; top: 200px; line-height: 1; white-space: nowrap; }
  .headline__main {
    display: block; font-family: "Roboto Condensed", sans-serif; font-weight: 500;
    font-size: 56px; color: var(--brand-blue); letter-spacing: -1.5px;
  }
  .headline__sub {
    display: block; margin-top: 8px; font-family: "Roboto", sans-serif; font-weight: 700;
    font-size: 60px; color: var(--brand-grey); letter-spacing: -0.5px;
  }
  .services {
    position: absolute; left: 26px; top: 372px; list-style: none;
    font-family: "Open Sans", sans-serif; font-weight: 500; font-size: 26px; color: var(--paper);
  }
  .services li { display: flex; align-items: center; gap: 10px; height: 40.7px; white-space: nowrap; }
  .services svg { width: 19px; height: 19px; flex: none; }
  .call {
    position: absolute; left: 28px; top: 613px; white-space: nowrap;
    font-family: "Montserrat", sans-serif; font-weight: 800; font-size: 40px; color: var(--paper);
  }
  .web {
    position: absolute; right: 34px; top: 618px; white-space: nowrap;
    font-family: "Open Sans", sans-serif; font-weight: 500; font-size: 32px; color: var(--brand-blue);
  }
</style>
</head>
<body>
<main class="advert">
  <svg class="advert__shapes" viewBox="0 0 1084 700" width="1084" height="700">
    <defs>
      <linearGradient id="photoTones" x1="0" y1="0" x2="1" y2="1">
        <stop offset="0" stop-color="var(--photo-light)"/>
        <stop offset="0.55" stop-color="var(--photo-mid)"/>
        <stop offset="1" stop-color="var(--photo-warm)"/>
      </linearGradient>
    </defs>
    <rect class="band-grey" x="0" y="600" width="1084" height="100" fill="var(--band-grey)"/>
    <polygon class="photo" role="img" aria-label="Technician measuring the bore of a red-painted flanged hub with a digital gauge in a workshop with a red workbench"
      points="592,0 1084,0 1084,585 590,585 424,345" fill="url(#photoTones)"/>
    <polygon class="panel-blue" points="0,352 402,352 657,700 0,700" fill="var(--brand-blue)"/>
    <line x1="0" y1="600" x2="584" y2="600" stroke="#4a8cc9" stroke-width="1"/>
  </svg>

  <div class="brand"><span class="brand__mark"></span>BOLT REMOVA LTD</div>

  <h1 class="headline">
    <span class="headline__main">PRODUCT TESTING</span>
    <span class="headline__sub">&amp; ANALYSIS</span>
  </h1>

  <ul class="services">
    <li><svg viewBox="0 0 20 20"><circle cx="10" cy="10" r="10" fill="#fff"/><path d="M5.5 10.3l3 3 6-6.3" fill="none" stroke="var(--brand-blue)" stroke-width="2.6"/></svg>Metallurgical testing</li>
    <li><svg viewBox="0 0 20 20"><circle cx="10" cy="10" r="10" fill="#fff"/><path d="M5.5 10.3l3 3 6-6.3" fill="none" stroke="var(--brand-blue)" stroke-width="2.6"/></svg>Bearing pre-load testing</li>
    <li><svg viewBox="0 0 20 20"><circle cx="10" cy="10" r="10" fill="#fff"/><path d="M5.5 10.3l3 3 6-6.3" fill="none" stroke="var(--brand-blue)" stroke-width="2.6"/></svg>Bore measurement</li>
    <li><svg viewBox="0 0 20 20"><circle cx="10" cy="10" r="10" fill="#fff"/><path d="M5.5 10.3l3 3 6-6.3" fill="none" stroke="var(--brand-blue)" stroke-width="2.6"/></svg>New product evaluation</li>
    <li><svg viewBox="0 0 20 20"><circle cx="10" cy="10" r="10" fill="#fff"/><path d="M5.5 10.3l3 3 6-6.3" fill="none" stroke="var(--brand-blue)" stroke-width="2.6"/></svg>Product analysis &amp; report</li>
  </ul>

  <p class="call">CALL US: 01614820517</p>
  <p class="web">www.bolt-remova.co.uk</p>
</main>
</body>
</html>
```